Breezeway Comfort business cards design

Need a business card design for a Heating and Air Conditioning business. I need these items included.
Business name: Breezeway Comfort
Owner: Marcus Tollefsen
License # 2874590
Phone number # 555-382-4071
Email: breezewaycomfortair@mailvista.example
Sales
Service
Installation
Maintenance

Heating and Air Conditioning

Requirements
Must have
• Company name , license number , phone number , email

```html
<!DOCTYPE html>
<html lang="en">
<head>
<meta charset="utf-8">
<title>Breezeway Comfort – Business Cards</title>
<link href="https://fonts.googleapis.com/css2?family=Saira:wght@400;500;600&display=swap" rel="stylesheet">
<style>
  :root {
    --brand-blue: #1c45a0;
    --deep-blue: #1b3f93;
    --accent-orange: #f39223;
    --accent-red: #ec4a4f;
    --card-white: #ffffff;
    --page-bg: #e9e6e1;
    --rule-blue: #1e3f8f;
  }
  * { box-sizing: border-box; margin: 0; padding: 0; }
  html, body {
    width: 1189px;
    height: 1200px;
    overflow: hidden;
    background: var(--page-bg);
    font-family: "Saira", sans-serif;
  }
  .card {
    position: absolute;
    left: 169px;
    width: 851px;
    height: 485px;
    border-radius: 34px;
    overflow: hidden;
    box-shadow: 0 6px 18px rgba(0,0,0,0.18);
  }
  .card--front {
    top: 100px;
    background: var(--card-white);
  }
  .card--front::after {
    content: "";
    position: absolute;
    left: 0; right: 0; bottom: 0;
    height: 10px;
    background: var(--deep-blue);
  }
  .card--back {
    top: 630px;
    background: var(--brand-blue);
  }
  .holder {
    position: absolute;
    left: 47px;
    top: 68px;
  }
  .holder__name {
    font-size: 29px;
    font-weight: 600;
    color: var(--brand-blue);
    letter-spacing: 0.5px;
    line-height: 1.1;
  }
  .holder__title {
    font-size: 19px;
    font-weight: 400;
    color: var(--accent-orange);
    letter-spacing: 0.6px;
    line-height: 1.1;
  }
  .brand {
    position: absolute;
    display: flex;
    align-items: center;
    gap: 14px;
    font-weight: 600;
    text-transform: uppercase;
    letter-spacing: 2px;
    line-height: 1;
  }
  .brand__dot {
    border-radius: 50%;
    flex: none;
  }
  .card--front .brand {
    right: 48px;
    top: 100px;
    font-size: 40px;
    color: var(--brand-blue);
  }
  .card--front .brand__dot {
    width: 40px; height: 40px;
    background: var(--accent-orange);
  }
  .card--back .brand {
    left: 0; right: 0;
    justify-content: center;
    top: 205px;
    font-size: 50px;
    color: var(--card-white);
  }
  .card--back .brand__dot {
    width: 50px; height: 50px;
    background: var(--accent-orange);
  }
  .divider {
    position: absolute;
    left: 47px;
    width: 755px;
    top: 343px;
    height: 2px;
    background: var(--rule-blue);
  }
  .contact {
    position: absolute;
    left: 47px;
    top: 392px;
    list-style: none;
  }
  .contact__item {
    display: flex;
    align-items: center;
    gap: 9px;
    font-size: 21px;
    font-weight: 500;
    color: var(--brand-blue);
    height: 28px;
  }
  .contact__icon { width: 22px; height: 22px; flex: none; }
  .license {
    position: absolute;
    right: 48px;
    top: 420px;
    font-size: 21px;
    font-weight: 500;
    color: var(--brand-blue);
    height: 28px;
    line-height: 28px;
  }
  .services {
    position: absolute;
    left: 0; right: 0;
    top: 343px;
    text-align: center;
    font-size: 23px;
    font-weight: 400;
    color: var(--card-white);
    letter-spacing: 0.4px;
  }
  .services__sep { margin: 0 6px; }
</style>
</head>
<body>

<section class="card card--front" aria-label="Business card front">
  <div class="holder">
    <p class="holder__name">Marcus Tollefsen</p>
    <p class="holder__title">Business Advisor</p>
  </div>

  <div class="brand">
    <span class="brand__dot"></span>
    <span class="brand__name">Breezeway Comfort</span>
  </div>

  <div class="divider"></div>

  <ul class="contact">
    <li class="contact__item">
      <svg class="contact__icon" viewBox="0 0 22 22" aria-hidden="true">
        <circle cx="11" cy="11" r="11" fill="var(--accent-orange)"/>
        <path d="M7.5 6.5c.6-.6 1.4-.5 1.8.1l1 1.5c.3.5.2 1.1-.2 1.4l-.6.5c.5 1.2 1.4 2.1 2.6 2.6l.5-.6c.3-.4.9-.5 1.4-.2l1.5 1c.6.4.7 1.2.1 1.8l-.7.7c-.7.7-1.8.8-2.7.3-2.2-1.2-3.9-2.9-5.1-5.1-.5-.9-.4-2 .3-2.7z" fill="#fff"/>
      </svg>
      <span>555-382-4071</span>
    </li>
    <li class="contact__item">
      <svg class="contact__icon" viewBox="0 0 22 22" aria-hidden="true">
        <circle cx="11" cy="11" r="11" fill="var(--accent-red)"/>
        <rect x="5.5" y="7" width="11" height="8" rx="1" fill="#fff"/>
        <path d="M5.8 7.4 11 11.4l5.2-4" fill="none" stroke="var(--accent-red)" stroke-width="1.1"/>
      </svg>
      <span>breezewaycomfortair@mailvista.example</span>
    </li>
  </ul>

  <p class="license">License # 2874590</p>
</section>

<section class="card card--back" aria-label="Business card back">
  <div class="brand">
    <span class="brand__dot"></span>
    <span class="brand__name">Breezeway Comfort</span>
  </div>
  <p class="services">
    Sales<span class="services__sep">|</span>Service<span class="services__sep">|</span>Installation<span class="services__sep">|</span>Maintenance
  </p>
</section>

</body>
</html>
```